HAIR EXTENSIONS

We need a web design for a company base in Chicago called Extensions by Corvina. We sale 100% human hair in Brazilian body wave deep wave straight or natural curl, Peruvian body wave straight or deep wave. Malaysian loose straight or body wave, in the chicago land.
We also ship hair to any city or country. We like to see design that use the colors pinks & grays, or would just like to see some design creative with colors thats inviting.

Also I'm using the tamsworth template, Home- banner contact us, about us, Features- product side/left sidebar, Shop- wish list /shopping cart/ tracking your order / checkout/ order received.
Porfolio-filterable 4column portfolio
Blog. Buy now

Industry/Entity Type

Hair

Number of Pages Required

4 page

Colors
aaaaaa
606060
dddddd
eea4c8
d3a5cc
b868aa
a6459a
ffc213
1b1b1b

Requirements
Must have
• I NEED THE DESIGNER TO DO THE 4 PAGE LIKE THIS.
• 1.HOME-PAGE BANNER CONTACT US SOME PRODUCT WITH SIDING IMAGES OF THE TOP PROUDCT
• 2.PRODUCT WITH SHOPPING CART- I WANT SIDING BARS FOR PRODUCT & SHOPPING CART WITH TRACKING YOUR ORDERS CHECK OUT & ORDER RECEIVED.
• 3.PORFOLIO PHOTO-I WANT A FEATURES FOR CUSTOMERS TO UPLOAN THERE PICTURE & BLOG ON THE PAGE
• 4.ABOUT US- TALK ABOUT ARE COMPAMY.
Nice to have
• hello designer
• I was working with a web developer for my site be for i came to pixelforgly & they build a site for me that i liked, You all can view it at www.Extensionsbycorvina.info
• long story short never could get them to finish the project after they got paid!!
• I know, why paid before its finish bad decision. So know I'm here starting over with you all.
• here is a list of my competition site
• www.tressvaultly.com
• www.lokawaves.com
• www.pellitashoppe.com
• So just to give some insight, I'm looking for something like the one i had builded.

```html
<!DOCTYPE html>
<html lang="en">
<head>
<meta charset="utf-8">
<title>Extensions by Corvina — Home</title>
<link rel="stylesheet" href="https://fonts.googleapis.com/css2?family=Raleway:wght@400;500;600;700;800&family=Open+Sans:wght@400;600&display=swap">
<style>
:root{
  --pink:#e0145a;
  --pink-soft:#f0709a;
  --wine:#3a0312;
  --ink:#1b1b1b;
  --text:#606060;
  --muted:#aaaaaa;
  --line:#dddddd;
  --tint:#f7eef2;
  --foot:#f1ecec;
  --white:#ffffff;
}
*{box-sizing:border-box;margin:0;padding:0}
html,body{width:707px;height:1200px;overflow:hidden;background:var(--white)}
body{position:relative;font-family:"Open Sans",Arial,sans-serif;color:var(--text)}
.abs{position:absolute}

/* top bar */
.topbar{left:0;top:0;width:707px;height:24px;border-bottom:1px solid var(--line)}
.social{left:78px;top:8px;display:flex;gap:12px}
.social span{width:8px;height:8px;background:var(--muted);border-radius:1px;display:block}
.social span:first-child{background:var(--pink)}
.account{left:470px;top:8px;font:500 6.5px "Raleway",sans-serif;color:var(--text);letter-spacing:.3px}
.cart{left:548px;top:4px;display:flex;align-items:center;gap:4px;font:600 6px "Raleway",sans-serif;color:var(--text)}

/* nav */
.logo{left:78px;top:34px;font:700 12px/1 "Raleway",sans-serif;color:var(--pink);letter-spacing:.2px}
.logo small{display:block;font-size:8.5px;margin-top:3px}
.nav{top:42px;font:500 7px "Raleway",sans-serif;color:var(--text);letter-spacing:.3px}
.nav.active{color:var(--pink)}
.search{left:590px;top:42px;font:500 6.5px "Raleway",sans-serif;display:flex;gap:3px;align-items:center;color:var(--text)}

/* hero */
.hero{left:0;top:72px;width:707px;height:289px;
  background:
    radial-gradient(ellipse 90px 150px at 120px 150px,rgba(214,190,150,.75),transparent 70%),
    radial-gradient(ellipse 70px 140px at 255px 190px,rgba(32,56,140,.85),transparent 70%),
    radial-gradient(ellipse 80px 150px at 405px 200px,rgba(40,40,48,.85),transparent 70%),
    radial-gradient(ellipse 70px 60px at 250px 60px,rgba(220,196,150,.7),transparent 70%),
    linear-gradient(180deg,#9fc0d4 0%,#b9cdd8 45%,#d8dee3 75%,#c7ccd0 100%)}
.hero-copy{right:61px;top:138px;text-align:right}
.hero-copy .l1{font:400 20px/1 "Raleway",sans-serif;color:var(--white);letter-spacing:-.3px}
.hero-copy .l2{font:800 25px/1.1 "Raleway",sans-serif;color:var(--pink);margin-top:2px}
.hero-copy .l3{font:600 11px "Raleway",sans-serif;color:var(--ink);margin-top:4px}

/* promo tiles */
.tile-photo{overflow:hidden}
.caption{left:0;right:0;bottom:0;height:36px;background:rgba(20,20,20,.62);padding:6px 8px}
.caption h4{font:500 9px "Raleway",sans-serif;color:var(--white)}
.caption p{font:400 5.5px "Open Sans",sans-serif;color:#ddd;margin-top:3px}
.caption p b{color:var(--pink);font-weight:600}
.tag{left:5px;height:12px;background:var(--pink);color:var(--white);font:600 6.5px/12px "Raleway",sans-serif;padding:0 7px}
.offer{display:flex;flex-direction:column;align-items:center;justify-content:center;text-align:center;color:var(--white)}
.offer .btn{border:1px solid var(--white);font:600 6.5px "Raleway",sans-serif;padding:4px 7px;margin-top:8px}

/* tabs */
.tabs{left:78px;top:634px;width:552px;height:13px;border-bottom:1px solid var(--line);display:flex;gap:25px;font:600 6.5px "Raleway",sans-serif;color:var(--muted)}
.tabs span.on{color:var(--pink);border-bottom:2px solid var(--pink);height:13px}
.arrow{top:630px;width:14px;height:14px;border:1px solid var(--line);font:600 8px/12px "Raleway",sans-serif;text-align:center;color:var(--ink);background:var(--white)}

/* products */
.card{width:126px}
.card .pic{width:126px;height:110px;background-color:var(--tint)}
.card .name{font:600 6.5px "Open Sans",sans-serif;color:var(--ink);margin-top:10px;display:flex;justify-content:space-between;padding:0 6px}
.card .name s{color:var(--text);font-weight:400}
.card .sub{font:400 5.5px "Open Sans",sans-serif;color:var(--text);display:flex;justify-content:space-between;align-items:baseline;padding:0 6px;margin-top:2px}
.card .sub b{color:var(--pink);font:400 7px "Open Sans",sans-serif}
.stars{padding:0 6px;margin-top:1px;color:var(--pink);font-size:7px;letter-spacing:-.5px}
.stars i{color:var(--muted);font-style:normal}
.card.first{border:1px solid var(--line);padding:2px;width:131px;height:159px}
.card.first .pic{height:90px}
.card.first .name{margin-top:7px}
.tools{display:flex;gap:4px;margin-top:3px;padding:0 2px;align-items:center}
.tools span{width:14px;height:14px;background:#f3f3f3;display:flex;align-items:center;justify-content:center}
.tools .buy{margin-left:auto;border:1px solid var(--pink);background:var(--white);width:17px;height:17px}

/* banner */
.banner{left:78px;top:998px;width:552px;height:104px;
  background:
    radial-gradient(ellipse 90px 70px at 70px 45px,rgba(235,235,235,.9),transparent 70%),
    linear-gradient(100deg,#b8b8b8 0%,#5a5a5a 22%,#262626 45%,#111 70%,#1e1e1e 100%)}
.banner-copy{left:441px;top:1021px}
.banner-copy .s{font:500 8px "Raleway",sans-serif;color:var(--white)}
.banner-copy .b{font:500 22px/1.1 "Raleway",sans-serif;color:var(--pink-soft);margin-top:2px;letter-spacing:-.5px}
.banner-copy .btn{display:inline-block;background:var(--pink);color:var(--white);font:600 7px "Raleway",sans-serif;padding:5px 10px;margin-top:6px}

/* footer */
.footer{left:0;top:1122px;width:707px;height:48px;background:var(--foot)}
.signup{left:78px;top:1135px;width:144px;height:22px;background:var(--white);display:flex;align-items:center;font:500 6px "Raleway",sans-serif}
.signup .lbl{padding:0 7px;color:var(--ink);border-right:1px solid var(--line)}
.signup .field{padding:0 6px;color:#c8c8c8;flex:1}
.signup .go{width:22px;height:22px;border:1px solid var(--pink);color:var(--pink);text-align:center;line-height:20px;font-size:10px}
.copy{left:260px;top:1137px;width:184px;text-align:center;font:400 6px "Open Sans",sans-serif;color:var(--text)}
.copy small{display:block;font-size:4.5px;margin-top:5px;color:var(--ink)}
.cards{left:498px;top:1140px;display:flex;gap:3px}
.cards span{width:18px;height:12px;border:1px solid #cfcfcf;background:var(--white);border-radius:2px;display:block}
.bottom{left:0;top:1170px;width:707px;height:30px;background:var(--pink);display:flex;justify-content:center;align-items:center;gap:8px;font:600 6.5px "Raleway",sans-serif;color:var(--white)}
.bottom em{font-style:normal;opacity:.7}
</style>
</head>
<body>

<div class="abs topbar"></div>
<div class="abs social" aria-label="Social links"><span></span><span></span><span></span><span></span><span></span><span></span></div>
<div class="abs account">LOGIN &nbsp;/&nbsp; SIGN UP</div>
<div class="abs cart">
  <svg width="14" height="14" viewBox="0 0 14 14"><path d="M2 4h10l-1 9H3z" fill="none" stroke="#e0145a" stroke-width="1.2"/><path d="M5 4V2.5a2 2 0 0 1 4 0V4" fill="none" stroke="#e0145a" stroke-width="1.2"/></svg>
  SHOPPING CART (0)
</div>

<div class="abs logo">EXTENSIONS<small>BY CORVINA</small></div>
<div class="abs nav active" style="left:226px">HOME</div>
<div class="abs nav" style="left:265px">ABOUT US</div>
<div class="abs nav" style="left:318px">HAIR SOLUTIONS</div>
<div class="abs nav" style="left:396px">PRODUCTS</div>
<div class="abs nav" style="left:452px">SHOP</div>
<div class="abs nav" style="left:490px">BLOG</div>
<div class="abs nav" style="left:527px">CONTACT US</div>
<div class="abs search">
  <svg width="8" height="8" viewBox="0 0 8 8"><circle cx="3.3" cy="3.3" r="2.5" fill="none" stroke="#1b1b1b"/><path d="M5.2 5.2L7.6 7.6" stroke="#1b1b1b"/></svg>SEARCH
</div>

<div class="abs hero" role="img" aria-label="Three models with long styled hair extensions in evening dresses"></div>
<div class="abs hero-copy">
  <div class="l1">FIND THE EXCELLENT</div>
  <div class="l2">QUALITY CLIP IN</div>
  <div class="l3">HAIR EXTENSIONS!</div>
</div>

<!-- promo tiles -->
<div class="abs tile-photo" style="left:78px;top:376px;width:174px;height:146px;background:radial-gradient(ellipse 60px 70px at 100px 60px,#d9a86a,transparent 75%),linear-gradient(135deg,#3e2e22,#7a5a3e 55%,#4a3a2c)" role="img" aria-label="Woman with wavy blonde hair wearing sunglasses">
  <div class="abs tag" style="top:98px">ACCESSORIES</div>
  <div class="abs caption"><h4>CLIP IN LOREM ISPUM</h4><p>Lorem ipsum dolor sit amet vesti <b>SHOP NOW</b></p></div>
</div>
<div class="abs offer" style="left:78px;top:536px;width:174px;height:82px;background:var(--wine);outline:1px solid var(--white);outline-offset:-4px">
  <div style="font:500 15px 'Raleway',sans-serif;letter-spacing:1.5px">FREE SHIPPING</div>
  <div style="font:400 6px 'Open Sans',sans-serif;color:#b58a98;margin-top:2px">on all orders over $50</div>
  <div class="btn">SHOP NOW!</div>
</div>
<div class="abs tile-photo" style="left:266px;top:376px;width:174px;height:242px;background:radial-gradient(ellipse 70px 110px at 90px 100px,#1e1614,transparent 75%),linear-gradient(160deg,#c98650,#8e5a38 45%,#c48a5c)" role="img" aria-label="Woman with long natural curly hair">
  <div class="abs tag" style="top:194px">NEW ARRIVALS</div>
  <div class="abs caption"><h4>HIGH QUALITY WIGS</h4><p>Lorem ipsum dolor sit amet vesti <b>SHOP NOW</b></p></div>
</div>
<div class="abs offer" style="left:454px;top:376px;width:176px;height:82px;background:var(--pink);outline:1px solid var(--white);outline-offset:-4px">
  <div style="font:500 14px 'Raleway',sans-serif">EXTRA 25% OFF SALE!</div>
  <div style="font:400 6.5px 'Open Sans',sans-serif;color:#f7b8cc;margin-top:2px">Use code: HAIR25</div>
  <div class="btn">SHOP NOW!</div>
</div>
<div class="abs tile-photo" style="left:454px;top:473px;width:176px;height:145px;background:radial-gradient(ellipse 50px 60px at 115px 55px,#c9a080,transparent 75%),linear-gradient(120deg,#3a3030,#a02a3a 30%,#6a5a52 60%,#8a7a6c)" role="img" aria-label="Smiling woman with long brown hair on a shopping street">
  <div class="abs tag" style="top:97px">LIMITTED OFFER</div>
  <div class="abs caption"><h4>SUMMER SALE! UP TO -70%</h4><p style="font:500 7px 'Raleway',sans-serif;color:var(--pink)">SHOP NOW</p></div>
</div>

<!-- tabs -->
<div class="abs tabs"><span class="on">FEATURED</span><span>NEW</span><span>SPECIALS</span><span>CUSTOM</span><span>TOP RATED</span></div>
<div class="abs arrow" style="left:598px">‹</div>
<div class="abs arrow" style="left:616px">›</div>

<!-- products row 1 -->
<div class="abs card first" style="left:77px;top:655px">
  <div class="pic" style="background-image:radial-gradient(ellipse 40px 22px at 50% 52%,#1c1f2a,rgba(28,31,42,.4) 60%,transparent 80%)" role="img" aria-label="Black hair bow"></div>
  <div class="tools">
    <span><svg width="8" height="7" viewBox="0 0 8 7"><path d="M4 7L.6 3.4A1.8 1.8 0 0 1 4 1.2a1.8 1.8 0 0 1 3.4 2.2z" fill="#bbb"/></svg></span>
    <span><svg width="8" height="8" viewBox="0 0 8 8"><path d="M1 3h5l-1.5-1.5M7 5H2l1.5 1.5" fill="none" stroke="#bbb"/></svg></span>
    <span><svg width="9" height="6" viewBox="0 0 9 6"><ellipse cx="4.5" cy="3" rx="4" ry="2.5" fill="none" stroke="#bbb"/><circle cx="4.5" cy="3" r="1.2" fill="#bbb"/></svg></span>
    <span class="buy"><svg width="10" height="9" viewBox="0 0 10 9"><path d="M0 1h2l1.2 5h5.3L10 2H3" fill="none" stroke="#e0145a"/><circle cx="4" cy="8" r=".9" fill="#e0145a"/><circle cx="8" cy="8" r=".9" fill="#e0145a"/></svg></span>
  </div>
  <div class="name">Bow Hair Extension <s>$ 165.00</s></div>
  <div class="sub">High Quality Wigs <b>$ 140.00</b></div>
  <div class="stars">★★★★★</div>
</div>
<div class="abs card" style="left:220px;top:658px">
  <div class="pic" style="background-image:radial-gradient(ellipse 30px 38px at 50% 50%,#b09262,rgba(176,146,98,.45) 60%,transparent 85%)" role="img" aria-label="Blonde braided bun hairpiece"></div>
  <div class="name">Bow Hair Extension <s>$ 165.00</s></div>
  <div class="sub">High Quality Wigs <b>$ 140.00</b></div>
  <div class="stars">★★★★<i>★</i></div>
</div>
<div class="abs card" style="left:361px;top:658px">
  <div class="pic" style="background-image:radial-gradient(ellipse 34px 42px at 55% 52%,#241612,rgba(36,22,18,.35) 55%,transparent 85%)" role="img" aria-label="Dark straight hair extension strand"></div>
  <div class="name">Bow Hair Extension <s>$ 165.00</s></div>
  <div class="sub">High Quality Wigs <b>$ 140.00</b></div>
  <div class="stars">★★★★<i>★</i></div>
</div>
<div class="abs card" style="left:501px;top:658px">
  <div class="pic" style="background-image:radial-gradient(ellipse 34px 34px at 58% 48%,#8a4a24,rgba(138,74,36,.35) 55%,transparent 85%)" role="img" aria-label="Auburn hair extension strand"></div>
  <div class="name">Bow Hair Extension <s>$ 165.00</s></div>
  <div class="sub">High Quality Wigs <b>$ 140.00</b></div>
  <div class="stars">★★★<i>★★</i></div>
</div>

<!-- products row 2 -->
<div class="abs card" style="left:80px;top:828px">
  <div class="pic" style="background-image:radial-gradient(ellipse 42px 26px at 50% 52%,#c98a58,rgba(201,138,88,.45) 60%,transparent 85%)" role="img" aria-label="Copper hair bow on a comb"></div>
  <div class="name">Bow Hair Extension <s>$ 165.00</s></div>
  <div class="sub">High Quality Wigs <b>$ 140.00</b></div>
  <div class="stars">★★★★★</div>
</div>
<div class="abs card" style="left:220px;top:828px">
  <div class="pic" style="background-image:radial-gradient(ellipse 32px 40px at 50% 50%,#7a4a2a,rgba(122,74,42,.45) 60%,transparent 85%)" role="img" aria-label="Brown braided bun hairpiece"></div>
  <div class="name">Bow Hair Extension <s>$ 165.00</s></div>
  <div class="sub">High Quality Wigs <b>$ 140.00</b></div>
  <div class="stars">★★★★<i>★</i></div>
</div>
<div class="abs card" style="left:361px;top:828px">
  <div class="pic" style="background-image:radial-gradient(ellipse 18px 50px at 50% 50%,#7a3c22,rgba(122,60,34,.45) 60%,transparent 90%)" role="img" aria-label="Brown clip-in hair weft set"></div>
  <div class="name">Bow Hair Extension <s>$ 165.00</s></div>
  <div class="sub">High Quality Wigs <b>$ 140.00</b></div>
  <div class="stars">★★★★<i>★</i></div>
</div>
<div class="abs card" style="left:501px;top:828px">
  <div class="pic" style="background-image:radial-gradient(ellipse 20px 50px at 52% 52%,#d9b47c,rgba(217,180,124,.45) 60%,transparent 90%)" role="img" aria-label="Blonde keratin tip hair bundle"></div>
  <div class="name">Bow Hair Extension <s>$ 165.00</s></div>
  <div class="sub">High Quality Wigs <b>$ 140.00</b></div>
  <div class="stars">★★★<i>★★</i></div>
</div>

<!-- banner -->
<div class="abs banner" role="img" aria-label="Black and white profile of a woman with long flowing dark hair"></div>
<div class="abs banner-copy">
  <div class="s">GET EVERYTHING YOU NEED FOR</div>
  <div class="b">HAIR EXTENSION!</div>
  <div class="btn">READ MORE</div>
</div>

<!-- footer -->
<div class="abs footer"></div>
<div class="abs signup"><span class="lbl">SIGN UP</span><span class="field">EMAIL ADDRESS</span><span class="go">→</span></div>
<div class="abs copy">© 2014 HAIR EXTENSIONS<small>PRIVACY POLICY | TERMS OF USE</small></div>
<div class="abs cards" aria-label="Accepted payment methods"><span></span><span></span><span></span><span></span><span></span><span></span></div>
<div class="abs bottom">HOME <em>|</em> PRICE LIST <em>|</em> PRODUCTS <em>|</em> OUR SERVICES <em>|</em> CONTACT <em>|</em> ON SALE! <em>|</em> JOBS LISTING <em>|</em> BLOG <em>|</em> SITEMAP</div>

</body>
</html>
```